CustomerPath UX Overhaul - redesign to improve visitor journeys and conversions

I need my website brought to life, professional and engaging.
I can supply as much pictures as needed to create enhancing visuals. I need your team to review the website and create a list of ideas of what you need from me to bring this vision to life.
The company does 3d modeling, 3d printing with FDM and resin printers, CAD design, 3d scanning.
My website is https://qtforgeworks.com/
Please review it and give me your best.
Target Market(s)
cosplayer, filmmakers, life size prints, custom designs, redesign and scanning, large and small scale prints, replicating
Industry/Entity Type
CAD Design, Additive Manufacturing, 3D Printing, 3D Scanning
Coding
Coded - Design and coding required
Number of Pages Required
3 page
Requirements
Must have
- Professional and clean look, inviting, eye grabber

```html
<!DOCTYPE html>
<html lang="en">
<head>
<meta charset="utf-8">
<title>QT Forgeworks – 3D Printing & Design</title>
<link rel="stylesheet" href="https://fonts.googleapis.com/css2?family=Kanit:wght@500;600&family=Poppins:wght@400;500&display=swap">
<style>
:root{
  --navy:#17145c;
  --navy-deep:#100e45;
  --cyan:#2cc9f2;
  --blue:#1a86e0;
  --ink:#111111;
  --muted:#666a75;
  --white:#ffffff;
  --line:#cfd3da;
  --head:'Kanit',sans-serif;
  --body:'Poppins',sans-serif;
}
*{box-sizing:border-box;margin:0;padding:0}
html,body{width:1200px;height:4320px;overflow:hidden}
body{position:relative;background:var(--white);font-family:var(--body);color:var(--ink)}
.abs{position:absolute}
.btn{position:absolute;display:flex;align-items:center;justify-content:center;color:var(--white);font-family:var(--head);font-weight:500;font-size:18px;text-decoration:none;background:linear-gradient(90deg,var(--cyan),var(--blue));clip-path:polygon(6% 0,100% 0,94% 100%,0 100%)}

/* header */
.site-header{position:absolute;left:0;top:0;width:1200px;height:80px;background:var(--white);z-index:5}
.nav a{position:absolute;top:31px;font-size:13px;color:var(--ink);text-decoration:none}
.nav a.active{color:var(--navy);font-weight:500}
.brand{position:absolute;left:505px;top:16px;width:190px;height:76px;background:var(--white);border-radius:0 0 14px 14px;display:flex;align-items:center;justify-content:center;gap:8px;font-family:var(--head);font-weight:600;font-size:19px;color:var(--navy);z-index:6}
.brand i{width:14px;height:14px;background:var(--cyan);border-radius:50%;display:block}

/* hero */
.hero-photo{left:0;top:80px;width:1200px;height:600px;background:linear-gradient(100deg,#1b1b1f 0%,#2c2a2e 45%,#5a4f46 70%,#2b2a2c 100%)}
.hero-title{left:62px;top:188px;width:690px;font-family:var(--head);font-weight:600;font-size:45px;line-height:58px;color:var(--white)}
.hero-title span{color:var(--cyan)}
.hero-sub{left:62px;top:379px;font-size:16px;color:var(--white)}

/* welcome */
.sec-title{position:absolute;left:0;width:1200px;text-align:center;font-family:var(--head);font-weight:500;font-size:37px;line-height:54px;color:var(--ink)}
.welcome-text{left:650px;top:908px;width:380px;font-size:12.5px;line-height:24px;color:var(--muted)}
.welcome-text p+p{margin-top:6px}

/* products */
.card{position:absolute;top:1485px;width:290px;height:409px;border:1.5px solid #6f6ca8;border-radius:10px;text-align:center;color:var(--white)}
.card .pic{position:absolute;left:8px;top:8px;width:272px;height:213px;border-radius:4px}
.card h3{position:absolute;left:36px;right:36px;top:237px;font-family:var(--head);font-weight:500;font-size:19px;line-height:27px}
.card .price{position:absolute;left:0;right:0;top:306px;font-size:15px}
.card .btn{left:67px;top:344px;width:155px;height:40px}
.arrow{position:absolute;top:1666px;width:46px;height:46px;border-radius:50%;background:var(--white)}

/* showcase */
.hex{position:absolute;width:258px;height:290px;clip-path:polygon(50% 0,100% 25%,100% 75%,50% 100%,0 75%,0 25%)}

/* mission */
.mission-panel{left:90px;top:2990px;width:435px;height:283px;background:rgba(40,40,44,.88);border-radius:12px;text-align:center;color:var(--white)}
.mission-panel h3{margin-top:103px;font-family:var(--head);font-weight:500;font-size:21px}
.mission-panel p{margin:12px auto 0;width:370px;font-size:12.5px;line-height:24px}

/* contact form */
.field{position:absolute;border:1px solid var(--line);border-radius:3px;background:var(--white);display:flex}
.field .ico{width:44px;border-right:1px solid var(--line);display:flex;align-items:center;justify-content:center}
.field .ico.top{align-items:flex-start;padding-top:12px}
.field span{padding:0 0 0 18px;font-size:12px;color:#333;display:flex;align-items:center}
.field.msg span{align-items:flex-start;padding-top:14px}

/* footer */
.site-footer{left:0;top:3990px;width:1200px;height:330px;background:var(--navy);color:var(--white)}
.foot-h{position:absolute;top:4050px;font-family:var(--head);font-weight:500;font-size:20px;color:var(--white)}
.foot-links a{position:absolute;left:62px;font-size:12px;color:var(--white);text-decoration:none}
.foot-item{position:absolute;font-size:12px;color:var(--white);line-height:25px}
.foot-item b{font-family:var(--head);font-weight:500;font-size:18px;letter-spacing:.3px}
.dot{position:absolute;width:38px;height:38px;border-radius:50%;background:var(--cyan)}
.social{position:absolute;left:843px;font-size:12px;color:var(--white)}
.rule{left:62px;top:4269px;width:1076px;height:1px;background:#47447e}
.copy{left:0;top:4286px;width:1200px;text-align:center;font-size:12px;color:var(--white)}
</style>
</head>
<body>

<header class="site-header">
  <nav class="nav">
    <a class="active" href="#" style="left:62px">Home</a>
    <a href="#" style="left:149px">About Us</a>
    <a href="#" style="left:255px">Featured Products</a>
    <a href="#" style="left:848px">Why Choose Us</a>
  </nav>
  <a class="btn" href="#" style="left:987px;top:22px;width:153px;height:40px">Contact Us</a>
</header>
<div class="brand"><i></i>QT Forgeworks</div>

<!-- hero -->
<div class="abs hero-photo" role="img" aria-label="3D printer printing a white twisted vase in a workshop"></div>
<svg class="abs" style="left:0;top:560px" width="1200" height="130" viewBox="0 0 1200 130">
  <polygon points="0,28 600,110 1200,28 1200,130 0,130" fill="#fff"/>
  <polygon points="0,28 600,110 600,102 0,18" fill="var(--cyan)"/>
  <polygon points="1200,28 600,110 600,102 1200,18" fill="var(--blue)"/>
  <polygon points="0,40 600,110 0,34" fill="#7fe0fb"/>
  <polygon points="1200,40 600,110 1200,34" fill="#7fe0fb"/>
</svg>
<h1 class="abs hero-title">Precision <span>3D Printing &amp; Design Services</span> - Personalized<br>Products &amp; Solutions</h1>
<p class="abs hero-sub">Transforming ideas into reality, one layer at a time.</p>
<a class="btn" href="#" style="left:62px;top:429px;width:152px;height:40px">Get a Quote</a>

<!-- welcome -->
<h2 class="sec-title" style="top:738px">Welcome QT Forgeworks</h2>
<svg class="abs" style="left:190px;top:820px" width="400" height="442" viewBox="0 0 400 442">
  <defs>
    <linearGradient id="frameGrad" x1="0" y1="0" x2="1" y2="1"><stop offset="0" stop-color="#2cc9f2"/><stop offset="1" stop-color="#1a86e0"/></linearGradient>
    <linearGradient id="lampGrad" x1="0" y1="0" x2="1" y2="1"><stop offset="0" stop-color="#153118"/><stop offset=".5" stop-color="#2f7a2c"/><stop offset="1" stop-color="#0d1a0f"/></linearGradient>
  </defs>
  <polygon points="200,4 396,114 396,328 200,438 4,328 4,114" fill="none" stroke="url(#frameGrad)" stroke-width="6"/>
  <polygon points="200,20 382,122 382,320 200,422 18,320 18,122" fill="url(#frameGrad)"/>
  <polygon points="200,30 372,128 372,314 200,412 28,314 28,128" fill="url(#lampGrad)" role="img" aria-label="Glowing green crystal lamp printed in 3D"/>
</svg>
<div class="abs welcome-text">
  <p>Discover expert 3D printing and engraving services. We turn your visions into reality, supporting veterans along the way!</p>
  <p>Lorem Ipsum has been the industry's standard dummy text ever since the 1500s, when an unknown printer took a galley of type and scrambled it to make a type specimen book. It has survived not only five centuries, but also the leap into electronic typesetting, remaining essentially unchanged.</p>
</div>
<a class="btn" href="#" style="left:650px;top:1128px;width:153px;height:40px">Get a Quote</a>

<!-- featured products band -->
<svg class="abs" style="left:0;top:1336px" width="1200" height="702" viewBox="0 0 1200 702">
  <polygon points="0,90 600,2 1200,90 1200,616 600,700 0,616" fill="var(--navy)"/>
  <polygon points="0,78 520,12 520,20 0,88" fill="var(--cyan)"/>
  <polygon points="1200,78 680,12 680,20 1200,88" fill="var(--cyan)"/>
  <polygon points="0,628 540,690 0,640" fill="var(--cyan)"/>
  <polygon points="1200,628 660,690 1200,640" fill="var(--cyan)"/>
  <polygon points="0,614 540,684 0,622" fill="var(--blue)"/>
  <polygon points="1200,614 660,684 1200,622" fill="var(--blue)"/>
</svg>
<h2 class="sec-title" style="top:1396px;color:var(--white)">Featured Products</h2>

<div class="card" style="left:151px">
  <div class="pic" role="img" aria-label="Row of bullet-shaped printed storage containers" style="background:linear-gradient(90deg,#8d9eb6,#c58a4d 35%,#a7adb5 55%,#9a3f3a 75%,#c9a24a)"></div>
  <h3>Bullet Replica Storage Containers</h3>
  <div class="price">$45.95</div>
  <a class="btn" href="#">Shop Now</a>
</div>
<div class="card" style="left:456px">
  <div class="pic" role="img" aria-label="Personalized dart holder stand with darts" style="background:linear-gradient(180deg,#c9ccd0,#8a7c5e 60%,#5c4a32)"></div>
  <h3>Personalized Dart Holder Stand</h3>
  <div class="price">$14.95</div>
  <a class="btn" href="#">Shop Now</a>
</div>
<div class="card" style="left:761px">
  <div class="pic" role="img" aria-label="Copper-coloured printed nut storage container" style="background:linear-gradient(135deg,#e4e6e8,#c9cdd0 45%,#b8703f 60%,#d9dcdf)"></div>
  <h3>Multi-Size Electrical Nut Storage Container</h3>
  <div class="price">$19.95</div>
  <a class="btn" href="#">Shop Now</a>
</div>
<svg class="arrow" style="left:59px" viewBox="0 0 46 46"><polygon points="28,14 16,23 28,32" fill="var(--navy)"/></svg>
<svg class="arrow" style="left:1095px;background:var(--cyan)" viewBox="0 0 46 46"><polygon points="18,14 30,23 18,32" fill="var(--white)"/></svg>

<!-- showcase -->
<h2 class="sec-title" style="top:2100px">Explore Our Creative Journey: A Showcase<br>Of 3D Printing And Design Projects</h2>
<div class="hex" style="left:60px;top:2249px;background:linear-gradient(160deg,#2d3f86,#6b86b6 50%,#2a6fb0)" role="img" aria-label="Printed desk lamp"></div>
<div class="hex" style="left:334px;top:2249px;background:linear-gradient(160deg,#1f1f22,#e8b5a6 45%,#a6d2c6 60%,#202023)" role="img" aria-label="Multicolour printed egg"></div>
<div class="hex" style="left:608px;top:2249px;background:linear-gradient(160deg,#263f8a,#3c63a8 45%,#b8304a 70%,#2a6fb0)" role="img" aria-label="Red printed basket"></div>
<div class="hex" style="left:882px;top:2249px;background:linear-gradient(160deg,#d7d6d3,#cfc3a8 50%,#25232a)" role="img" aria-label="Printed skull model"></div>
<div class="hex" style="left:196px;top:2484px;background:linear-gradient(160deg,#d9d9db,#3a3838 50%,#c7552c 75%,#2a2a2c)" role="img" aria-label="Desktop 3D printer"></div>
<div class="hex" style="left:470px;top:2484px;background:linear-gradient(160deg,#e3e4e6,#3a3d44 45%,#38a9c9 65%,#1a1b1f)" role="img" aria-label="Printer nozzle printing a blue part"></div>
<div class="hex" style="left:744px;top:2484px;background:linear-gradient(160deg,#c8c5c9,#2c2b30 45%,#d9a7b5 65%,#26252b)" role="img" aria-label="Person working with a 3D printer"></div>

<!-- mission -->
<div class="abs" style="left:0;top:2849px;width:1200px;height:572px;background:linear-gradient(100deg,#3a3a3f,#6c6b70 45%,#b8a9a3 65%,#2e2d31);clip-path:polygon(0 15%,50% 0,100% 15%,100% 86%,50% 100%,0 86%)" role="img" aria-label="Person adjusting a 3D printer in a studio"></div>
<svg class="abs" style="left:0;top:2849px" width="1200" height="572" viewBox="0 0 1200 572">
  <polygon points="0,84 530,8 530,16 0,96" fill="var(--cyan)"/>
  <polygon points="1200,84 670,8 670,16 1200,96" fill="var(--cyan)"/>
  <polygon points="0,492 560,566 0,504" fill="var(--cyan)"/>
  <polygon points="1200,492 640,566 1200,504" fill="var(--cyan)"/>
</svg>
<div class="abs mission-panel">
  <svg class="abs" style="left:194px;top:38px" width="46" height="46" viewBox="0 0 46 46"><circle cx="21" cy="25" r="17" fill="none" stroke="var(--cyan)" stroke-width="4"/><circle cx="21" cy="25" r="9" fill="none" stroke="var(--cyan)" stroke-width="4"/><circle cx="21" cy="25" r="3" fill="var(--cyan)"/><line x1="21" y1="25" x2="38" y2="8" stroke="var(--cyan)" stroke-width="3"/></svg>
  <h3>Our Mission</h3>
  <p>At QT Forgeworks, our mission is to turn visions into reality, layer by layer. As a small family-owned business based in Ridgevale, we are dedicated to providing high-quality 3D printing and engraving services for all kinds of projects.</p>
</div>

<!-- contact -->
<h2 class="sec-title" style="top:3486px">Contact Us</h2>
<div class="field" style="left:292px;top:3573px;width:301px;height:42px">
  <div class="ico"><svg width="14" height="14" viewBox="0 0 14 14"><circle cx="7" cy="4" r="3.5" fill="var(--navy)"/><path d="M1 14c0-4 3-6 6-6s6 2 6 6z" fill="var(--navy)"/></svg></div><span>First Name *</span></div>
<div class="field" style="left:607px;top:3573px;width:303px;height:42px">
  <div class="ico"><svg width="14" height="14" viewBox="0 0 14 14"><polygon points="0,6 14,0 9,14 7,8" fill="var(--navy)"/></svg></div><span>Last Name *</span></div>
<div class="field" style="left:292px;top:3630px;width:301px;height:42px">
  <div class="ico"><svg width="14" height="14" viewBox="0 0 14 14"><path d="M2 1l3 0 1 3-2 1.5c1 2 2.5 3.5 4.5 4.5L10 8l3 1 0 3c-6 1-12-5-11-11z" fill="var(--navy)"/></svg></div><span>Phone no *</span></div>
<div class="field" style="left:607px;top:3630px;width:303px;height:42px">
  <div class="ico"><svg width="14" height="12" viewBox="0 0 14 12"><rect x="0" y="1" width="14" height="10" rx="1" fill="var(--navy)"/><polyline points="1,2 7,7 13,2" fill="none" stroke="#fff" stroke-width="1.3"/></svg></div><span>E-mail *</span></div>
<div class="field msg" style="left:292px;top:3687px;width:618px;height:75px">
  <div class="ico top"><svg width="14" height="13" viewBox="0 0 14 13"><path d="M0 0h14v9H5l-3 4V9H0z" fill="var(--navy)"/></svg></div><span>Message *</span></div>
<a class="btn" href="#" style="left:525px;top:3791px;width:150px;height:42px">Submit Now</a>

<!-- footer -->
<svg class="abs" style="left:0;top:3920px" width="1200" height="90" viewBox="0 0 1200 90">
  <polygon points="0,88 600,18 1200,88 1200,90 0,90" fill="var(--navy)"/>
  <polygon points="0,78 560,20 0,86" fill="var(--cyan)"/>
  <polygon points="1200,78 640,20 1200,86" fill="var(--cyan)"/>
  <polygon points="0,70 560,16 0,74" fill="var(--blue)"/>
  <polygon points="1200,70 640,16 1200,74" fill="var(--blue)"/>
</svg>
<div class="abs site-footer"></div>
<div class="brand" style="top:3908px;border-radius:14px;height:66px"><i></i>QT Forgeworks</div>

<h4 class="foot-h" style="left:62px">Quick Links</h4>
<nav class="foot-links">
  <a href="#" style="top:4096px">Home</a>
  <a href="#" style="top:4124px">About Us</a>
  <a href="#" style="top:4153px">Featured Product</a>
  <a href="#" style="top:4181px">Why Choose Us</a>
  <a href="#" style="top:4210px">Contact Us</a>
</nav>

<h4 class="foot-h" style="left:427px">Contact Us</h4>
<svg class="dot" style="left:427px;top:4104px" viewBox="0 0 38 38"><path d="M12 10l4 0 1.5 4-2.5 2c1.5 3 3.5 5 6.5 6.5l2-2.5 4 1.5 0 4c-9 1.5-17-6.5-15.5-15.5z" fill="#fff"/></svg>
<div class="foot-item" style="left:481px;top:4096px">Call to Action :<br><b>1 (555) 014.2271</b></div>
<svg class="dot" style="left:427px;top:4181px" viewBox="0 0 38 38"><circle cx="19" cy="19" r="9" fill="none" stroke="#fff" stroke-width="2.5"/><polyline points="19,14 19,19 23,21" fill="none" stroke="#fff" stroke-width="2.5"/></svg>
<div class="foot-item" style="left:481px;top:4172px">Working Hours :<br>Mon-Fri : 9am-5pm<br>Sat-Sun : Closed</div>

<h4 class="foot-h" style="left:791px">follow Us</h4>
<div class="dot" style="left:791px;top:4099px"></div><span class="social" style="top:4110px">Chatterly</span>
<div class="dot" style="left:791px;top:4150px"></div><span class="social" style="top:4161px">Chirpster</span>
<div class="dot" style="left:791px;top:4204px"></div><span class="social" style="top:4215px">WorkNetly</span>

<div class="abs rule"></div>
<p class="abs copy">Copyright © 2024 QT Forgeworks - All Rights Reserved.</p>

</body>
</html>
```